Marrowby's Vacation Rentals Business Card

Multi Million dollar villa rentals in the Dominican Republic.

Industry/Entity Type

Business

Contact Information for Business Card

I am looking for a high-end look around my company name/logo (see attached) on one side incorporating the following info: first and last name, title, address, phone #, email and company website. On the backside I want to add a full color picture of one of our villas (see attached).

```html
<!DOCTYPE html>
<html lang="en">
<head>
<meta charset="UTF-8">
<title>Marrowby's Vacation Rentals – Business Card</title>
<link href="https://fonts.googleapis.com/css2?family=Lato:wght@400;700;900&display=swap" rel="stylesheet">
<style>
  :root {
    --backdrop: #e9e6e1;
    --navy: #1f2733;
    --navy-soft: #2b3442;
    --orange: #f26a21;
    --white: #ffffff;
    --ink: #3a3f47;
    --sky: #8dbde3;
    --villa: #ebe7de;
    --pool: #2e8fd6;
  }
  * { margin: 0; padding: 0; box-sizing: border-box; }
  html, body {
    width: 1200px; height: 900px; overflow: hidden;
    background: var(--backdrop);
    font-family: 'Lato', sans-serif;
  }
  .canvas {
    position: relative; width: 1200px; height: 900px;
    display: flex; flex-direction: column; align-items: center; justify-content: center; gap: 56px;
  }
  .card {
    position: relative; width: 660px; height: 378px;
    background: var(--white); overflow: hidden;
    box-shadow: 0 10px 30px rgba(0,0,0,.18);
  }
  .card svg.layer { position: absolute; inset: 0; }

  /* back side */
  .card-back { background: var(--navy); }

  /* front side */
  .brand {
    position: absolute; left: 40px; top: 62px;
    display: flex; align-items: center; gap: 10px;
  }
  .brand-dot { width: 26px; height: 26px; border-radius: 50%; background: var(--orange); }
  .brand-name {
    font-weight: 900; font-size: 21px; color: var(--navy); line-height: 1.05;
  }
  .brand-name small { display: block; font-size: 12px; letter-spacing: 2px; text-transform: uppercase; }

  .name-bar {
    position: absolute; left: 0; top: 128px; width: 300px; height: 50px;
    background: var(--navy); border-radius: 0 26px 26px 0;
    display: flex; align-items: center; padding-left: 40px; gap: 14px;
  }
  .name-icon {
    width: 28px; height: 28px; background: var(--white); border-radius: 3px;
    display: flex; align-items: center; justify-content: center;
  }
  .person-name { color: var(--white); font-weight: 700; font-size: 20px; line-height: 1; }
  .person-title { color: var(--orange); font-size: 12px; margin-top: 3px; }

  .contacts { position: absolute; left: 40px; top: 200px; list-style: none; }
  .contacts li {
    display: flex; align-items: center; gap: 14px;
    font-size: 14px; color: var(--ink); height: 34px;
  }
  .contacts li.address { height: 46px; line-height: 1.25; }
  .contact-icon {
    flex: none; width: 24px; height: 24px; background: var(--orange); border-radius: 3px;
    display: flex; align-items: center; justify-content: center;
  }
</style>
</head>
<body>
<main class="canvas">

  <!-- Back: villa photograph side -->
  <section class="card card-back">
    <svg class="layer" width="660" height="378" viewBox="0 0 660 378">
      <defs>
        <linearGradient id="villaTones" x1="0" y1="0" x2="0" y2="1">
          <stop offset="0" stop-color="var(--sky)"/>
          <stop offset="0.3" stop-color="#cfe0ea"/>
          <stop offset="0.5" stop-color="var(--villa)"/>
          <stop offset="0.72" stop-color="#c9c4b5"/>
          <stop offset="0.8" stop-color="var(--pool)"/>
          <stop offset="1" stop-color="#1f6fb3"/>
        </linearGradient>
      </defs>
      <rect width="660" height="378" fill="var(--navy)"/>
      <path d="M0 88 L600 40 L660 40 L660 300 L40 320 L0 320 Z" fill="url(#villaTones)" role="img" aria-label="Photograph of a white luxury villa with terracotta roof, palm trees and a blue swimming pool"/>
      <path d="M470 30 Q560 20 630 30 Q650 60 620 90" fill="none" stroke="var(--white)" stroke-width="2" opacity=".8"/>
      <path d="M560 330 Q600 270 660 250" fill="none" stroke="var(--white)" stroke-width="2" opacity=".8"/>
    </svg>
  </section>

  <!-- Front: contact side -->
  <section class="card card-front">
    <svg class="layer" width="660" height="378" viewBox="0 0 660 378">
      <defs>
        <linearGradient id="villaDim" x1="0" y1="0" x2="0" y2="1">
          <stop offset="0" stop-color="#4d5866"/>
          <stop offset="0.55" stop-color="#3a4451"/>
          <stop offset="0.85" stop-color="#2c4d6c"/>
          <stop offset="1" stop-color="#1f5f8e"/>
        </linearGradient>
      </defs>
      <path d="M360 0 H660 V350 L438 348 Q408 348 404 320 L360 0 Z" fill="url(#villaDim)" role="img" aria-label="Darkened photograph of the villa terrace and pool"/>
    </svg>

    <div class="brand">
      <span class="brand-dot"></span>
      <div class="brand-name">Marrowby's<small>Vacation Rentals</small></div>
    </div>

    <div class="name-bar">
      <span class="name-icon">
        <svg width="18" height="18" viewBox="0 0 18 18"><circle cx="9" cy="6" r="3.5" fill="var(--navy)"/><path d="M2.5 16 Q9 8 15.5 16 Z" fill="var(--navy)"/></svg>
      </span>
      <div>
        <div class="person-name">Elliot Harmon</div>
        <div class="person-title">Marketing manager</div>
      </div>
    </div>

    <ul class="contacts">
      <li>
        <span class="contact-icon"><svg width="14" height="14" viewBox="0 0 14 14"><path d="M3 1 L5 1 L6 4 L4.5 5.2 Q6 8.5 8.8 9.5 L10 8 L13 9 L13 11 Q12 13 10 13 Q2 11 1 3 Q1 1 3 1 Z" fill="var(--white)"/></svg></span>
        01-611 472305
      </li>
      <li>
        <span class="contact-icon"><svg width="14" height="14" viewBox="0 0 14 14"><path d="M1 6.5 L13 1 L9 13 L6.5 8 Z" fill="var(--white)"/></svg></span>
        hello@marrowbys.com
      </li>
      <li>
        <span class="contact-icon"><svg width="14" height="14" viewBox="0 0 14 14"><g fill="none" stroke="var(--white)" stroke-width="1.8"><rect x="1.5" y="6" width="6" height="4" rx="2" transform="rotate(-45 4.5 8)"/><rect x="6.5" y="4" width="6" height="4" rx="2" transform="rotate(-45 9.5 6)"/></g></svg></span>
        www.marrowbys.com
      </li>
      <li class="address">
        <span class="contact-icon"><svg width="14" height="14" viewBox="0 0 14 14"><path d="M7 13 Q2 7.5 2 5 A5 5 0 0 1 12 5 Q12 7.5 7 13 Z" fill="var(--white)"/><circle cx="7" cy="5" r="1.8" fill="var(--orange)"/></svg></span>
        <span>Co-level, 80412,<br>517, Harbor Street, NY-961420</span>
      </li>
    </ul>
  </section>

</main>
</body>
</html>
```